Not Your Average Diet Book Cover Design

I need a book cover designed for a project titled:
Title: Quiet Harbor Method
Sub-title: The Gentle Road To Lasting Change With Your Plate
Author: Darlene Forsythe
Designation: Not a Doctor
The book is a look at 8 trendy diets (Brevard, Whole Foods, Paleo, Keto, Mediterranean, Sugar Free, Alkaline and Intermittent Fasting), with each chapter covering the pros and cons of one.
The theme throughout the book is that, when approached as a diet, they are each doomed to failure. When sustainability and lifestyle are taken into consideration, however, any one of them (or a combination of two or more) can lead to overall health and weight management.
Vegetables, mindset and habit creation are 3 of the "overlap" factors implied in the title.
I have uploaded a temporary cover that I am using as a placeholder at the moment. I do NOT want anything like it. (Use the tagline above, not the one in the sample cover).
Please, NO images of scales, stomachs, or anything else that is super cliche for the weight loss industry.
This is a full length book, written in a conversation tone, that I want to stand out from the a) copy and pasted online "experts" and b) doctors and fitpros who think it's their way or the highway. I want it to be welcoming and accessible.
I want the book to appeal to an audience who is currently struggling with their health and most likely failed at many diets in the past.
I will need a print cover for a 6"x 9" Printloom book, as well as a Veltra cover and an Tavrel cover.
I would like all source files, including any fonts used. For delivery, placeholder text can be used for the back cover.
Target Market(s)
Male & Female
Overweight
Unhealthy, but not severely so
Have tried diets before and failed
Age: 25-55 (average)
Income: $30-50k USD
Marital status: Single OR not entirely satisfied with the relationship
Location: Canada, USA, Australia, UK
Industry/Entity Type
Health And Wellness
Colors
Designer to choose colors to be used in the design.
Requirements
Must have
- Title: Quiet Harbor Method
- Sub-title: The Gentle Road To Lasting Change With Your Plate
- Author: Darlene Forsythe
- Designation: Not a Doctor
Nice to have
- A welcoming, understanding feeling
- Implications of holistic health
Should not have
- Images:
- - Scale or measuring tapes, etc
- - stomachs/abs
- - yoga or any silhouettes
- A look similar to the sample.

```html
<!DOCTYPE html>
<html lang="en">
<head>
<meta charset="utf-8">
<title>Quiet Harbor Method — Book Cover</title>
<link rel="stylesheet" href="https://fonts.googleapis.com/css2?family=Lora:ital,wght@0,600;0,700;1,500&family=Nunito+Sans:wght@400;600;700&display=swap">
<style>
  :root {
    --cream: #fbf6ee;
    --harbor: #1f4e5a;
    --sage: #8fb996;
    --teal: #4fa3a5;
    --coral: #f08a5d;
    --sand: #efe3cf;
    --muted: #5b7279;
  }
  html, body { margin: 0; padding: 0; overflow: hidden; background: var(--cream); }
  .cover {
    position: relative;
    width: 800px;
    height: 1200px;
    overflow: hidden;
    background: var(--cream);
    font-family: "Nunito Sans", Arial, sans-serif;
    color: var(--harbor);
  }
  .title {
    position: absolute;
    left: 70px; top: 80px;
    width: 660px;
    margin: 0;
    font-family: "Lora", Georgia, serif;
    font-weight: 700;
    font-size: 92px;
    line-height: 1.02;
    letter-spacing: -1px;
  }
  .title .accent { color: var(--teal); }
  .subtitle {
    position: absolute;
    left: 72px; top: 312px;
    width: 600px;
    margin: 0;
    font-weight: 600;
    font-size: 26px;
    line-height: 1.35;
    color: var(--muted);
  }
  .rule {
    position: absolute;
    left: 72px; top: 292px;
    width: 90px; height: 5px;
    border-radius: 3px;
    background: var(--coral);
  }
  .overlap {
    position: absolute;
    left: 150px; top: 440px;
    width: 500px; height: 500px;
  }
  .overlap circle { mix-blend-mode: multiply; }
  .diet-band {
    position: absolute;
    left: 0; top: 972px;
    width: 800px; height: 58px;
    background: var(--sand);
  }
  .diet-list {
    position: absolute;
    left: 40px; top: 972px;
    width: 720px;
    margin: 0;
    text-align: center;
    font-size: 15px;
    font-weight: 600;
    line-height: 58px;
    letter-spacing: 0.3px;
    color: var(--harbor);
    white-space: nowrap;
  }
  .author {
    position: absolute;
    left: 0; top: 1062px;
    width: 800px;
    margin: 0;
    text-align: center;
    font-family: "Lora", Georgia, serif;
    font-weight: 600;
    font-size: 36px;
    line-height: 1.2;
  }
  .designation {
    position: absolute;
    left: 0; top: 1114px;
    width: 800px;
    margin: 0;
    text-align: center;
    font-family: "Lora", Georgia, serif;
    font-style: italic;
    font-weight: 500;
    font-size: 20px;
    color: var(--coral);
  }
</style>
</head>
<body>
<main class="cover">
  <h1 class="title">Quiet Harbor<br><span class="accent">Method</span></h1>
  <div class="rule"></div>
  <p class="subtitle">The Gentle Road To Lasting Change With Your Plate</p>

  <svg class="overlap" viewBox="0 0 500 500" aria-hidden="true">
    <circle cx="170" cy="180" r="150" fill="var(--sage)" opacity="0.8"/>
    <circle cx="330" cy="180" r="150" fill="var(--teal)" opacity="0.7"/>
    <circle cx="250" cy="320" r="150" fill="var(--coral)" opacity="0.7"/>
    <circle cx="250" cy="227" r="14" fill="var(--cream)"/>
  </svg>

  <div class="diet-band"></div>
  <p class="diet-list">Brevard · Whole Foods · Paleo · Keto · Mediterranean · Sugar Free · Alkaline · Intermittent Fasting</p>

  <p class="author">Darlene Forsythe</p>
  <p class="designation">Not a Doctor</p>
</main>
</body>
</html>
```